Casa Vero Inspections Business Card

I need a business card for my new company. The company is going to provide home inspections. The name of the company is Casa Vero Inspections. I am not sure if I want a single sided card or a double. I have a logo already that I want to incorporate into the card design. I was wondering if I should incorporate a catch phrase on my card or not. If I did the phrase would be "The Thorough Choice for Every Home You Buy" but i am unsure how or if to use it on a card. The following information needs to be on the card.
Home Inspection
My Name: Marcus T. Wolford Phone Number: 555-301-7762 Email: mwolford@casaveroinspections.com Website: www.casaveroinspections.com NY HI License # 27300519462

```html
<!DOCTYPE html>
<html lang="en">
<head>
<meta charset="utf-8">
<title>Casa Vero Inspections – Business Card</title>
<link rel="stylesheet" href="https://fonts.googleapis.com/css2?family=Arimo:wght@400;700&family=Montserrat:wght@700&display=swap">
<style>
  :root {
    --page-bg: #151515;
    --card-bg: #1f1f20;
    --sky: #6cbfe8;
    --white: #f4f4f4;
    --text: #f0f0f0;
  }
  * { margin: 0; padding: 0; box-sizing: border-box; }
  html, body {
    width: 1200px; height: 1059px; overflow: hidden;
    background: var(--page-bg);
    font-family: "Arimo", Arial, sans-serif;
    color: var(--text);
  }
  .card {
    position: absolute;
    background: var(--card-bg);
    border-radius: 13px;
    overflow: hidden;
  }
  .card--front { left: 257px; top: 89px; width: 687px; height: 390px; }
  .card--back  { left: 254px; top: 547px; width: 693px; height: 393px; }

  .brand {
    font-family: "Arimo", Arial, sans-serif;
    font-weight: 700;
    color: var(--white);
    line-height: 1.05;
    display: flex; align-items: center; gap: 12px;
  }
  .brand__mark { width: 16px; height: 16px; background: var(--sky); flex: none; }
  .card--front .brand {
    position: absolute; right: 32px; top: 120px;
    font-size: 31px; text-align: right;
  }
  .card--back .brand {
    position: absolute; left: 0; right: 0; top: 190px;
    justify-content: center; font-size: 46px; text-align: center;
  }

  .holder { position: absolute; left: 32px; top: 194px; }
  .holder__name {
    font-family: "Montserrat", Arial, sans-serif;
    font-weight: 700; font-size: 23px; color: var(--sky); letter-spacing: 0.3px;
  }
  .holder__title { font-size: 17px; margin-top: 4px; }

  .divider {
    position: absolute; left: 32px; right: 32px; top: 263px;
    height: 1px; background: var(--sky);
  }

  .contacts { position: absolute; left: 32px; top: 279px; list-style: none; font-size: 17px; }
  .contacts li { display: flex; align-items: center; gap: 5px; height: 27px; }
  .contacts svg { width: 13px; height: 13px; fill: var(--sky); flex: none; }

  .license { position: absolute; right: 32px; top: 333px; font-size: 17px; }

  .accent-band { position: absolute; left: 0; bottom: 0; width: 687px; height: 14px; }

  .tagline {
    position: absolute; left: 0; right: 0; top: 338px;
    text-align: center; font-size: 17px;
  }
</style>
</head>
<body>
  <section class="card card--front">
    <div class="brand"><span class="brand__mark"></span><span>Casa Vero<br>Inspections</span></div>

    <div class="holder">
      <div class="holder__name">Marcus T. Wolford</div>
      <div class="holder__title">CEO/Founder</div>
    </div>

    <div class="divider"></div>

    <ul class="contacts">
      <li>
        <svg viewBox="0 0 24 24" aria-hidden="true"><path d="M6.6 10.8a15 15 0 0 0 6.6 6.6l2.2-2.2a1 1 0 0 1 1-.25 11.4 11.4 0 0 0 3.6.57 1 1 0 0 1 1 1V20a1 1 0 0 1-1 1A17 17 0 0 1 3 4a1 1 0 0 1 1-1h3.5a1 1 0 0 1 1 1c0 1.25.2 2.45.57 3.57a1 1 0 0 1-.25 1z"/></svg>
        555-301-7762
      </li>
      <li>
        <svg viewBox="0 0 24 24" aria-hidden="true"><path d="M2 6.5V19h20V6.5l-10 7.5z M3 5l9 6.8L21 5z"/></svg>
        mwolford@casaveroinspections.com
      </li>
      <li>
        <svg viewBox="0 0 24 24" aria-hidden="true"><path d="M12 2a10 10 0 1 0 0 20 10 10 0 0 0 0-20zm-1 17.9A8 8 0 0 1 4.2 10.2L9 15v1a2 2 0 0 0 2 2zm6.9-2.5A2 2 0 0 0 16 16h-1v-3a1 1 0 0 0-1-1H8v-2h2a1 1 0 0 0 1-1V7h2a2 2 0 0 0 2-2v-.4a8 8 0 0 1 2.9 12.8z"/></svg>
        www.casaveroinspections.com
      </li>
    </ul>

    <div class="license">NY HI License # 27300519462</div>

    <svg class="accent-band" viewBox="0 0 687 14" preserveAspectRatio="none" aria-hidden="true">
      <polygon points="0,0 349,0 331,14 0,14" fill="#6cbfe8"/>
      <polygon points="360,0 687,0 687,14 340,14" fill="#f4f4f4"/>
    </svg>
  </section>

  <section class="card card--back">
    <div class="brand"><span class="brand__mark"></span><span>Casa Vero Inspections</span></div>
    <p class="tagline">The Thorough Choice for Every Home You Buy</p>
  </section>
</body>
</html>
```